Modern Dental Appointment Reminder/Business Card

We already have a beautiful logo and icon picked from here on ArtisanHive, now we need someone to make them into a beautiful business card for us! This business card will also function as an appointment reminder card for patients. It will be double sided and must include:
Front
-Contact Info as Follows:
(Gavin R Moss, DDS
Family and Cosmetic Dentistry
2946 S 1320 E Ste 400
Farmington, Utah 84137)
-Our Logo or Icon (your choice, if Icon must write "Bellmere Dental" below it like in the example file)
Back
-"You're Invited!"
-"Your next appointment is on"
-Place to write date & time
-"Please call 24hrs ahead if appointment is to be cancelled
-Our Icon

Logo and Icon to be used are attached below, along with an example of what we need.
Please do NOT use lots of red! We want the red to just be an accent. Please use grey, white, or even a muted teal for the majority of the card.

Industry/Entity Type

Dentistry

Contact Information for Business Card

Gavin R Moss, DDS
2946 S 1320 E Ste 400
Farmington, Utah 84137

Colors
cfeae6

Requirements
Should not have
• Lots of red!

```html
<!DOCTYPE html>
<html lang="en">
<head>
<meta charset="utf-8">
<title>Bellmere Dental – Business &amp; Appointment Card</title>
<link rel="stylesheet" href="https://fonts.googleapis.com/css2?family=Merriweather:wght@400;700;900&family=Arimo:wght@400&display=swap">
<style>
  :root {
    --page-bg: #e9e9e7;
    --card-white: #ffffff;
    --accent-red: #a82a2d;
    --warm-grey: #55504a;
    --text-grey: #5d5a57;
    --rule-grey: #b9b6b2;
    --faint-grey: #efeeed;
  }
  * { box-sizing: border-box; margin: 0; padding: 0; }
  html, body { width: 1200px; height: 1015px; overflow: hidden; }
  body {
    background: var(--page-bg);
    display: flex; flex-direction: column; align-items: center; justify-content: center;
    gap: 56px;
  }
  .card {
    position: relative;
    width: 760px; height: 434px;
    background: var(--card-white);
    box-shadow: 0 10px 24px rgba(0,0,0,.18);
    overflow: hidden;
  }

  /* ---------- Appointment side ---------- */
  .appt-header {
    height: 92px; background: var(--accent-red);
    display: flex; align-items: flex-end; justify-content: center; padding-bottom: 16px;
  }
  .appt-title {
    font-family: 'Merriweather', serif; font-weight: 900;
    color: var(--card-white); font-size: 30px; letter-spacing: 1px;
  }
  .appt-body { position: relative; height: 250px; padding: 30px 0 0 150px; }
  .appt-watermark {
    position: absolute; left: 50%; top: 12px; transform: translateX(-50%);
    width: 226px; height: 226px; border-radius: 50%;
    background: var(--faint-grey);
  }
  .appt-lead {
    position: relative;
    font-family: 'Merriweather', serif; font-size: 30px; color: var(--text-grey);
  }
  .appt-field {
    position: relative; display: flex; align-items: flex-end;
    margin-top: 30px; margin-left: 60px; width: 400px;
    font-family: 'Arimo', sans-serif; font-size: 26px; color: #a6a3a0;
  }
  .appt-field .write-line { flex: 1; border-bottom: 1px solid var(--rule-grey); margin-left: 10px; height: 26px; }
  .appt-footer {
    position: absolute; left: 0; right: 0; bottom: 0; height: 92px;
    background: var(--warm-grey);
    display: flex; align-items: center; justify-content: center;
  }
  .appt-note { font-family: 'Arimo', sans-serif; font-size: 17px; color: var(--card-white); }
  .appt-footer::after {
    content: ""; position: absolute; left: 0; right: 0; top: 0; height: 38px;
    background: var(--warm-grey);
  }

  /* ---------- Contact side ---------- */
  .brand {
    position: absolute; left: 70px; top: 150px; width: 260px;
    display: flex; flex-direction: column; align-items: center; gap: 18px;
  }
  .brand-mark { width: 70px; height: 70px; border-radius: 50%; background: var(--warm-grey); }
  .brand-name {
    font-family: 'Merriweather', serif; font-weight: 400;
    font-size: 30px; color: var(--accent-red); letter-spacing: 1px; white-space: nowrap;
  }
  .divider {
    position: absolute; left: 370px; top: 80px; width: 1px; height: 150px;
    background: linear-gradient(var(--card-white), var(--rule-grey), var(--card-white));
  }
  .contact { position: absolute; left: 400px; top: 95px; color: var(--text-grey); }
  .contact-name {
    font-family: 'Merriweather', serif; font-weight: 900; font-size: 22px;
    color: var(--accent-red); text-transform: uppercase;
  }
  .contact-name .credential { font-weight: 400; color: var(--text-grey); text-transform: none; margin-left: 4px; }
  .contact-role, .contact-address { font-family: 'Arimo', sans-serif; font-size: 18px; line-height: 1.3; }
  .contact-address { margin-top: 18px; }
  .band-red {
    position: absolute; left: 0; bottom: 0; width: 520px; height: 20px; background: var(--accent-red);
  }
  .band-grey {
    position: absolute; right: 0; bottom: 0; width: 240px; height: 72px; background: var(--warm-grey);
  }
  .band-grey::before {
    content: ""; position: absolute; left: 0; top: 0; width: 6px; height: 100%; background: var(--card-white);
  }
</style>
</head>
<body>

  <section class="card card-appointment">
    <header class="appt-header"><h1 class="appt-title">YOU'RE INVITED!</h1></header>
    <div class="appt-body">
      <div class="appt-watermark" aria-hidden="true"></div>
      <p class="appt-lead">Your next appointment is on</p>
      <div class="appt-field"><span>TIME</span><span class="write-line"></span></div>
      <div class="appt-field"><span>DATE</span><span class="write-line"></span></div>
    </div>
    <footer class="appt-footer"><p class="appt-note">Please call 24hrs ahead if appointment is to be cancelled</p></footer>
  </section>

  <section class="card card-contact">
    <div class="brand">
      <span class="brand-mark" aria-hidden="true"></span>
      <span class="brand-name">BELLMERE DENTAL</span>
    </div>
    <div class="divider" aria-hidden="true"></div>
    <div class="contact">
      <p class="contact-name">Gavin R Moss<span class="credential">DDS</span></p>
      <p class="contact-role">Family and Cosmetic Dentistry</p>
      <p class="contact-address">2946 S 1320 E Ste 400<br>Farmington, Utah 84137</p>
    </div>
    <div class="band-red" aria-hidden="true"></div>
    <div class="band-grey" aria-hidden="true"></div>
  </section>

</body>
</html>
```